Quiet Iron Hours - Cover for a book exploring how modern men think and feel

The book explores what men in today's world think and feel, and what they want from society and the people in their lives. The idea is to put the focus on men and how they're dealing with a world in which patriarchy is rightly under scrutiny and women are finding and using their voice. How do men feel in the company of more empowered women? What do men want from the women in their lives (not talking about sex here)? Why are men more likely to take their own lives, not coping well with mental health issues?

Target Market(s)

Men and Women

Font styles to use
Other font styles liked:
• Clean and non-fussy font

Colors

Designer to choose colors to be used in the design.

Requirements
Must have
• A silhouette of a man or multiple men from diverse backgrounds and age groups
Nice to have
• The image must be bold and yet understated in its simplicity.
Should not have
• Nothing sexual or suggestive.

```html
<!DOCTYPE html>
<html lang="en">
<head>
<meta charset="utf-8">
<title>Quiet Iron Hours — Book Cover</title>
<link rel="stylesheet" href="https://fonts.googleapis.com/css2?family=Anton&family=Arimo:wght@400;700&display=swap">
<style>
  :root {
    --stage: #d9d6d2;
    --paper: #f1f0ee;
    --paper-shade: #e6e3df;
    --red: #e8303a;
    --red-deep: #d9242e;
    --ink: #141414;
    --white: #ffffff;
  }
  * { margin: 0; padding: 0; box-sizing: border-box; }
  html, body {
    width: 1200px; height: 939px; overflow: hidden;
    background: var(--stage);
  }
  .cover {
    position: absolute;
    left: 320px; top: 40px;
    width: 560px; height: 860px;
    background: linear-gradient(180deg, var(--paper) 40%, var(--paper-shade) 100%);
    overflow: hidden;
    box-shadow: 0 10px 30px rgba(0,0,0,0.18);
  }
  .red-band {
    position: absolute; left: 0; top: 0;
    width: 560px; height: 345px;
  }
  .title-kicker {
    position: absolute; left: 0; top: 78px; width: 100%;
    display: flex; align-items: center; justify-content: center; gap: 18px;
  }
  .kicker-rule { width: 140px; height: 2px; background: var(--white); }
  .kicker-word {
    font-family: "Anton", sans-serif;
    font-size: 66px; line-height: 1; color: var(--ink);
    letter-spacing: 1px;
  }
  .title-main {
    position: absolute; left: 0; top: 160px; width: 100%;
    text-align: center;
    font-family: "Anton", sans-serif;
    font-size: 108px; line-height: 1; color: var(--white);
    letter-spacing: 1px;
  }
  .figure-silhouette {
    position: absolute; left: 240px; top: 372px;
    width: 80px; height: 196px;
    background: var(--ink);
    border-radius: 18px 18px 4px 4px;
  }
  .subtitle {
    position: absolute; left: 0; top: 614px; width: 100%;
    text-align: center;
    font-family: "Arimo", sans-serif;
    font-size: 27px; line-height: 1.28; color: var(--ink);
  }
  .subtitle .accent { color: var(--red); }
  .author {
    position: absolute; left: 0; top: 770px; width: 100%;
    text-align: center;
    font-family: "Arimo", sans-serif; font-weight: 700;
    font-size: 34px; letter-spacing: 3px; color: var(--ink);
  }
</style>
</head>
<body>
  <main class="cover">
    <svg class="red-band" viewBox="0 0 560 345" aria-hidden="true">
      <defs>
        <linearGradient id="bandFill" x1="0" y1="0" x2="1" y2="1">
          <stop offset="0" stop-color="#d9242e"/>
          <stop offset="1" stop-color="#e8303a"/>
        </linearGradient>
      </defs>
      <path fill="url(#bandFill)"
        d="M0 0 H560 V335 L540 332 L520 338 L498 330 L470 336 L440 327 L410 333 L380 326 L352 331 L320 324 L290 329 L262 322 L230 316 L200 320 L168 312 L140 316 L110 308 L82 312 L54 304 L28 308 L0 300 Z"/>
    </svg>

    <div class="title-kicker">
      <span class="kicker-rule"></span>
      <span class="kicker-word">QUIET</span>
      <span class="kicker-rule"></span>
    </div>
    <h1 class="title-main">IRON HOURS</h1>

    <div class="figure-silhouette" role="img" aria-label="Silhouette of a headless man in a dark suit and tie, standing with hands behind his back"></div>

    <p class="subtitle">
      Frank Notes On What<br>
      <span class="accent">MEN CARRY</span><br>
      And Rarely Say Aloud
    </p>

    <p class="author">MEERA KALSANG</p>
  </main>
</body>
</html>
```